Modellprojekt in der Jugendhilfe sucht für Abschlussbroschüre ansprechendes Design
Zielgruppe
Wir sind ein Jugendhilfeträger und haben kürzlich ein dreijähriges Modellprojekt 'Qualitätsmarke-Gemeinsame Familienbegleitung' (Signet 'QM_Anerkennung' liegt anbei) beendet. Zielgruppen sind zum Einen Kinder und Jugendliche, die in Erziehungshilfe-Wohngruppen leben und zum Anderen Fach- und Führungskräfte in der Kinder- und Jugendhilfe. Über Ablauf und Schlussfolgerungen aus dem abgeschlossenen Modellprojekt soll eine 30-seitige Broschüre mit dem Titel 'Hier wächst Mitsprache' Untertitel 'Ein Wegweiser zur Qualitätsmarke' Auskunft geben.
Aufgabenstellung
- Broschüre im DIN A4 - Format,
- Dummy-Text für Projektstruktur und -beteiligte,
- Formschönes und dynamisches Design,
- Platzhalter für eigene Bilder (max. 3 pro Seite),
- die 6 Einrichtungslogos in einer Reihe auf dem Deckblatt vorne (unten),
- Der Broschüreninhalt ist in der PDF 'Kurzvorstellung enthalten',
- Vorgaben zum CD im PDF 'Hauptmanual KWF',
- Das KWF-Signet, wie im Manual beschrieben,
- das ebenfalls hochgeladene Gütesiegel kommt auf das Deckblatt

```html
<!DOCTYPE html>
<html lang="de">
<head>
<meta charset="utf-8">
<title>Hier wächst Mitsprache – Broschüre</title>
<link href="https://fonts.googleapis.com/css2?family=Fira+Sans+Condensed:wght@300;400;500&family=Source+Serif+4:opsz,wght@8..60,400&display=swap" rel="stylesheet">
<style>
:root{
  --blue:#1d6fb8;
  --green:#2e9a3b;
  --lavender:#dfe3f3;
  --ink:#2b2b2b;
  --paper:#ffffff;
  --bg:#ececec;
  --photo-blue:#5f7f9e;
}
*{margin:0;padding:0;box-sizing:border-box}
html,body{width:1200px;height:848px;overflow:hidden;background:var(--bg)}
.canvas{position:relative;width:1200px;height:848px}
.sans{font-family:"Fira Sans Condensed",sans-serif}
.body-copy{font-family:"Source Serif 4",serif;font-size:5.3px;line-height:8.2px;color:var(--ink);text-align:justify}
.abs{position:absolute}

/* spread */
.spread{left:390px;top:51px;width:759px;height:537px;background:var(--paper)}
.story-title{left:35px;top:92px;font-family:"Fira Sans Condensed",sans-serif;font-weight:300;font-size:22px;color:var(--blue)}
.story-sub{left:35px;top:136px;width:300px;font-family:"Fira Sans Condensed",sans-serif;font-size:8.5px;line-height:12px;color:var(--blue)}
.col{position:absolute}
.col h4{font-family:"Fira Sans Condensed",sans-serif;font-weight:400;font-size:7px;line-height:8.5px;color:var(--blue);margin:0 0 5px}
.img-slot{position:absolute}
.tip-box{left:185px;top:290px;width:138px;height:202px;background:var(--lavender);border-radius:5px;padding:10px 8px}
.tip-box h3{font-family:"Fira Sans Condensed",sans-serif;font-weight:500;font-size:10px;color:var(--green);margin-bottom:7px}
.tip-box li{list-style:none;position:relative;padding-left:6px;margin-bottom:6px;font-family:"Fira Sans Condensed",sans-serif;font-size:5px;line-height:7.5px;font-weight:500;color:var(--ink)}
.tip-box li::before{content:"";position:absolute;left:0;top:1px;width:2px;height:5px;background:var(--green)}
.hero{left:389px;top:9px;width:359px;height:242px;background:linear-gradient(120deg,#8a6a52 0%,#b58b6c 45%,#3d3430 100%)}
.hero-quote{right:20px;top:82px;width:200px;text-align:right;font-family:"Fira Sans Condensed",sans-serif;font-weight:300;font-size:8.8px;line-height:16.5px;letter-spacing:.6px;color:#fff;text-transform:uppercase}
.side-box{left:584px;top:203px;width:138px;height:174px;background:var(--lavender);border-radius:5px;padding:12px 8px}
.side-box h4{font-family:"Fira Sans Condensed",sans-serif;font-weight:400;font-size:7px;line-height:8.5px;color:var(--blue);width:80px;margin-bottom:16px}
.portrait{left:672px;top:178px;width:66px;height:66px;border-radius:50%;border:3px solid var(--green);background:radial-gradient(circle at 50% 45%,#c98f72,#7a4a36)}
.folio{font-family:"Fira Sans Condensed",sans-serif;font-size:4.5px;color:#9aa3b5}

/* cover */
.cover{left:57px;top:213px;width:403px;height:569px;background:var(--paper)}
.cover-photo{left:0;top:0;width:403px;height:310px;background:linear-gradient(160deg,#27548a 0%,#6d8fb1 40%,#c79a7e 60%,#3a5f86 100%)}
.seal{left:55px;top:54px}
.cover-title{left:56px;top:380px;font-family:"Fira Sans Condensed",sans-serif;font-weight:500;font-size:23px;line-height:29px;color:var(--blue)}
.partners{left:56px;top:474px;width:320px}
.partner{position:absolute;display:flex;align-items:center;gap:3px;font-family:"Fira Sans Condensed",sans-serif;font-weight:500;font-size:5.4px;line-height:6.5px;color:var(--ink)}
.partner i{display:block;width:7px;height:7px;border-radius:50%;background:#e5612a;flex:none}
.kwf{position:absolute;left:0;top:-2px;display:flex;gap:5px;align-items:flex-start}
.kwf .mark{width:28px;height:56px;background:var(--photo-blue)}
.kwf span{font-family:"Fira Sans Condensed",sans-serif;font-size:6.4px;line-height:7.5px;color:var(--ink);width:55px}
</style>
</head>
<body>
<div class="canvas">

  <section class="abs spread" aria-label="Innenseiten Erfolgsstory">
    <h1 class="abs story-title">Erfolgsstory</h1>
    <p class="abs story-sub">Blindtext steht hier Best Practise – Vorstellung vor Ort, z.B. Selbstportrait/ Rollenbeschreibung eines Gruppensprechers</p>

    <div class="col" style="left:70px;top:168px;width:108px">
      <h4>Wir erzählen gern von unserem Alltag, heute und hier</h4>
      <p class="body-copy">Wir treffen uns jede Woche in der Gruppe und sprechen über das, was uns wichtig ist. Jeder darf etwas sagen und alle hören zu. So entstehen neue Ideen für den Alltag im Haus und für gemeinsame Ausflüge am Wochenende.</p>
      <p class="body-copy" style="margin-top:8px">Die Betreuer begleiten uns dabei, aber die Entscheidungen treffen wir selbst. Das war am Anfang ungewohnt, heute ist es ganz normal für uns alle.</p>
    </div>
    <div class="img-slot" role="img" aria-label="Foto: lachende Jugendliche sitzen zusammen" style="left:70px;top:290px;width:102px;height:105px;background:linear-gradient(135deg,#6f8fa8,#c9a58c 60%,#2f4b66)"></div>
    <div class="col" style="left:70px;top:412px;width:108px">
      <p class="body-copy">Im Gruppenrat planen wir Regeln, Feste und die Gestaltung der Räume. Jede Stimme zählt, und wir stimmen offen ab. Wer mag, übernimmt eine Aufgabe für die Woche.</p>
      <p class="body-copy" style="margin-top:6px">Am Ende jedes Monats schauen wir gemeinsam zurück.</p>
    </div>

    <div class="col" style="left:185px;top:168px;width:138px">
      <p class="body-copy">Seit Beginn des Projekts hat sich viel verändert. Wir haben gelernt, unsere Wünsche klar zu benennen und Kompromisse zu finden. Die Fachkräfte nehmen unsere Vorschläge ernst und setzen sie gemeinsam mit uns um. Besonders wichtig war die Wahl der Gruppensprecher, die unsere Anliegen in der Einrichtung vertreten. Sie treffen sich regelmäßig mit der Leitung und berichten danach in der Gruppe. So wissen alle, was besprochen wurde und wie es weitergeht. Auch schwierige Themen haben Platz, wenn es Streit gibt, suchen wir zusammen nach einer Lösung, die für alle passt und fair bleibt.</p>
    </div>

    <aside class="abs tip-box">
      <h3>Good to knows</h3>
      <ul>
        <li>Jede Gruppe wählt zwei Sprecher, die ihre Anliegen in die Runde der Leitung bringen.</li>
        <li>Beschwerden können offen oder anonym über den Briefkasten im Flur eingereicht werden und werden innerhalb einer Woche beantwortet.</li>
        <li>Der Gruppenrat tagt einmal im Monat und hält seine Beschlüsse schriftlich fest.</li>
        <li>Neue Kinder erhalten am ersten Tag eine Mappe mit ihren Rechten und allen Ansprechpartnern im Haus. Fragen sind jederzeit willkommen.</li>
      </ul>
    </aside>

    <div class="abs hero" role="img" aria-label="Foto: junger Mann zeigt mit der Hand das Victory-Zeichen">
      <p class="abs hero-quote">Wir reden mit und gestalten unser Zuhause selbst, jeden Tag ein Stück mehr, gemeinsam mit allen, die hier wohnen und arbeiten.</p>
    </div>

    <aside class="abs side-box">
      <h4>Stimmen aus dem Team</h4>
      <p class="body-copy">Mitsprache ist bei uns kein Extra, sondern Teil der täglichen Arbeit. Wir haben erlebt, wie die Jugendlichen Verantwortung übernehmen und stolz auf ihre Ideen sind. Das verändert auch unsere Haltung als Fachkräfte. Wir fragen früher nach, hören genauer hin und planen gemeinsam statt für die Gruppe. Nicht alles gelingt sofort, doch jeder kleine Schritt zeigt, dass sich der Weg lohnt und alle davon profitieren.</p>
    </aside>
    <div class="abs portrait" role="img" aria-label="Porträtfoto einer lächelnden Mitarbeiterin"></div>

    <div class="col" style="left:431px;top:264px;width:144px">
      <p class="body-copy">Die Auswertung zeigt, dass die Beteiligung in allen Gruppen gewachsen ist. Jugendliche nennen vor allem die offenen Gespräche und die festen Zeiten für ihre Anliegen als hilfreich im Alltag.</p>
      <h4 style="margin-top:12px">Was wir aus drei Jahren Projektarbeit gelernt haben</h4>
      <p class="body-copy">Klare Abläufe geben Sicherheit. Wenn alle wissen, wann und wo sie mitreden können, nutzen sie diese Möglichkeit auch. Wichtig ist, dass Ergebnisse sichtbar werden und Vorschläge nicht im Sande verlaufen. Dafür braucht es feste Rückmeldungen.</p>
      <h4 style="margin-top:10px">Ausblick auf die nächsten Schritte im Verbund</h4>
      <p class="body-copy">Die Einrichtungen wollen die Erfahrungen teilen und weitere Gruppen einbinden.</p>
    </div>
    <div class="col" style="left:584px;top:390px;width:138px">
      <p class="body-copy">Für die kommenden Jahre planen wir gemeinsame Schulungen für Fachkräfte und Jugendliche. Dabei sollen die Gruppensprecher selbst als Trainer auftreten und von ihren Erfahrungen berichten. So entsteht ein Netzwerk, das voneinander lernt und die Qualitätsmarke im Alltag lebendig hält.</p>
    </div>

    <p class="abs folio" style="left:70px;top:513px">Hier wächst Mitsprache – Wege zur Qualitätsmarke</p>
    <p class="abs folio" style="left:603px;top:513px">Hier wächst Mitsprache – Wege zur Qualitätsmarke &nbsp;| 3</p>
  </section>

  <section class="abs cover" aria-label="Titelseite">
    <div class="abs cover-photo" role="img" aria-label="Foto: viele Hände übereinander als Zeichen des Zusammenhalts"></div>
    <svg class="abs seal" width="64" height="64" viewBox="0 0 64 64" role="img" aria-label="Qualitätssiegel">
      <circle cx="32" cy="32" r="31" fill="#ffffff" opacity=".85"/>
      <circle cx="32" cy="32" r="22" fill="#1f6b5a" stroke="#2e9a3b" stroke-width="3"/>
    </svg>
    <h2 class="abs cover-title">Hier wächst Mitsprache –<br>Wege zur Qualitätsmarke</h2>

    <div class="abs partners">
      <div class="kwf"><div class="mark"></div><span>KWF<br>Gruppe Küstenverbund für Wohlfahrt</span></div>
      <div class="partner" style="left:95px;top:6px"><i></i>Familienwerk<br>Nordufer</div>
      <div class="partner" style="left:167px;top:6px"><i></i>Jugendhilfe<br>Lindenhof</div>
      <div class="partner" style="left:238px;top:8px"><i></i>Kinderhaus Wiesengrund</div>
      <div class="partner" style="left:95px;top:40px"><i style="background:#f0b400"></i>Wohngruppen<br>Seeblick</div>
      <div class="partner" style="left:167px;top:40px"><i></i>Hilfen<br>Marschland</div>
      <div class="partner" style="left:238px;top:40px"><i></i>Jugendverbund<br>Heidekamp</div>
    </div>
  </section>

</div>
</body>
</html>
```